Female Vocalist Needs Design for Music Album

Hi, my name is Corinna Vashti and I need a design for my first album. It will be a Digipak, 4 panel (1tray) and disk. (I will be using pressforge to print the CDs. Please see http://www.pressforgeworks.example/templates/ for digipak template and design specs.)
The musical genre of this album is sacred/religious/gospel- solo mezzo soprano with solo piano accompaniment. The musical style is traditional with a few pieces that have a more contemporary feel.
I would like to see designs that have the following:
FRONT COVER (Panel 1):
Photo of the artist, name of the artist, and album title: Lift Up Your Lantern (see attached). Try to create the feeling that the artist is alone in the shadows and light from heaven is pouring down onto her face as she is crying out to God. Font for the artist name in a flowing script-like calligraphic handwriting.
BACK COVER (Panel 2):
Photo of the artist and the track list (see attached).
INSIDE PANEL (Panel 3 - Back side of Front Cover):
Dedication, Special Thank You, and Credits (see attached). May include a picture of the recording artist.
CD TRAY PANEL (Panel 4):
Background using the design elements and colors used throughout, but no photos of the artist.
CD DISK DESIGN:
Name of the artist and album title on background using design elements and colors used throughout, but no photos of the artist.
I would like to see some 'sophistication' (for lack of a better word) in the design. It may be elegantly simple, or more elaborate- something well thought out down to the choice of font style and placement. Please feel free to use your imagination and creativity. The final design should enhance the photo of the artist and go with the overall prayerful theme of the album title.
Attached are some design examples that I found interesting.
Updates
For those who did not get the album text, I just re posted the attachment. I apologize...I thought I had attached it, but apparently accidentally detached it when I was editing the brief. We added the track lengths and made a few corrections and additions to the album text. Please see the attached Word Document "Corinna Vashti Album Text" on the brief. Thank you.
Target Market(s)
Target market are Christians and people of faith.
Industry/Entity Type
Religious
Requirements
Must have
- For the front cover, please use photo P1140955. For the back cover, please use photo P1140515.
Nice to have
- Retouch the artist photo to remove any incidental blemishes. Remove any distracting elements like in the photo backgrounds, unless you think it goes with the design theme. Crop photos as necessary. Please use your best judgement on whether to keep the photo background or to enhance it, add on to it, or completely change the backgrounds and/or to add other design elements and ornamentation. If another background is used, make sure it does not clash with what the artist is wearing and there is still good contrast between the photo and the background. One idea could be to use a off-white/light grey background on the outside covers and red on the inside covers. Ornamentation should be light, translucent, and subtle.
Should not have
- The design should NOT include any religious symbols or icons such as crosses, fishes, doves, etc., and no cartoon-like clip art.

```html
<!DOCTYPE html>
<html lang="en">
<head>
<meta charset="utf-8">
<title>Lift Up Your Lantern — Corinna Vashti</title>
<link rel="stylesheet" href="https://fonts.googleapis.com/css2?family=Libre+Baskerville:wght@700&family=Pinyon+Script&family=Great+Vibes&display=swap">
<style>
  :root {
    --red-deep: #b8121c;
    --red-bright: #e01f26;
    --red-glow: #ee3a33;
    --cream: #f6ebb4;
    --gold: #d8c27a;
    --gold-dark: #a8893f;
    --spine-white: #ffffff;
    --frame-dark: #1a1a12;
    --text-shadow: #3a0505;
  }
  html, body {
    margin: 0;
    padding: 0;
    overflow: hidden;
    background: #ffffff;
  }
  .digipak {
    position: relative;
    width: 1200px;
    height: 450px;
    overflow: hidden;
  }
  .panel {
    position: absolute;
    top: 0;
    height: 450px;
    background: radial-gradient(ellipse at 50% 45%, var(--red-glow) 0%, var(--red-bright) 45%, var(--red-deep) 100%);
  }
  .back-cover { left: 0; width: 545px; }
  .front-cover { left: 627px; width: 573px; }
  .ornament-border {
    position: absolute;
    inset: 0;
    border: 18px solid rgba(216, 160, 120, 0.18);
    pointer-events: none;
  }
  .back-portrait {
    position: absolute;
    left: 40px;
    top: 120px;
    width: 470px;
    height: 330px;
    border-radius: 45% 45% 0 0;
    background: radial-gradient(ellipse at 45% 40%, rgba(60, 40, 40, 0.55) 0%, rgba(80, 30, 30, 0.35) 55%, rgba(180, 20, 30, 0) 80%);
  }
  .track-list {
    position: absolute;
    left: 44px;
    top: 22px;
    margin: 0;
    padding: 0;
    list-style: none;
    font-family: "Libre Baskerville", "Times New Roman", serif;
    font-weight: 700;
    font-size: 17.5px;
    line-height: 1.2;
    color: var(--cream);
    text-shadow: 1px 1px 2px var(--text-shadow);
  }
  .track-list li { position: absolute; left: 0; white-space: nowrap; }
  .track-list .wrap { white-space: normal; width: 480px; }
  .spine {
    position: absolute;
    left: 545px;
    top: 0;
    width: 82px;
    height: 450px;
    background: var(--spine-white);
  }
  .spine-text {
    position: absolute;
    left: 41px;
    top: 225px;
    transform: translate(-50%, -50%) rotate(90deg);
    white-space: nowrap;
    display: flex;
    align-items: center;
    gap: 14px;
    color: var(--gold-dark);
  }
  .spine-title { font-family: "Great Vibes", cursive; font-size: 30px; }
  .spine-name { font-family: "Pinyon Script", cursive; font-size: 20px; }
  .spine-dot { width: 8px; height: 8px; border-radius: 50%; background: var(--gold-dark); }
  .artist-name {
    position: absolute;
    left: 0;
    width: 100%;
    top: 42px;
    margin: 0;
    text-align: center;
    font-family: "Pinyon Script", cursive;
    font-weight: 400;
    font-size: 40px;
    color: var(--gold);
    text-shadow: 1px 1px 2px var(--text-shadow);
  }
  .cover-photo {
    position: absolute;
    left: 25px;
    top: 127px;
    width: 528px;
    height: 250px;
    box-sizing: border-box;
    border: 4px solid var(--frame-dark);
    border-radius: 6px;
    background:
      radial-gradient(ellipse at 42% 62%, rgba(150, 90, 60, 0.8) 0%, rgba(60, 40, 20, 0.6) 25%, rgba(0, 0, 0, 0) 45%),
      linear-gradient(90deg, #0c0c08 0%, #1c1c12 35%, #5d5a3e 62%, #c8c6a2 80%, #7f7d5a 100%);
    box-shadow: 0 0 10px rgba(0, 0, 0, 0.5);
  }
  .album-title {
    position: absolute;
    left: 0;
    width: 100%;
    top: 362px;
    margin: 0;
    text-align: center;
    font-family: "Great Vibes", cursive;
    font-weight: 400;
    font-size: 60px;
    line-height: 1;
    color: var(--cream);
    text-shadow: 2px 2px 2px #222, 0 0 4px #000;
  }
</style>
</head>
<body>
<main class="digipak">
  <section class="panel back-cover">
    <div class="ornament-border" role="img" aria-label="Light gold swirling filigree border ornament"></div>
    <div class="back-portrait" role="img" aria-label="Faded translucent portrait of the artist behind the track list"></div>
    <ol class="track-list">
      <li style="top:0">1. Lift Up Your Lantern / Rock of Ages</li>
      <li style="top:47px">2. His Eye is On the Sparrow</li>
      <li style="top:96px">3. Give Them All to Jesus Medley</li>
      <li style="top:138px">4. Great is Thy Faithfulness / Day By Day</li>
      <li style="top:178px">5. There is a Fountain</li>
      <li class="wrap" style="top:216px">6. Are You Ready for Jesus to Come / Redemption Draweth Nigh</li>
      <li style="top:282px">7. A Quiet Place</li>
      <li style="top:322px">8. Midnight Cry</li>
      <li style="top:352px">9. The Holy City</li>
      <li style="top:392px">10. The Lord's Prayer</li>
    </ol>
  </section>

  <aside class="spine">
    <div class="spine-text">
      <span class="spine-title">Lift Up Your Lantern</span>
      <span class="spine-dot"></span>
      <span class="spine-name">Corinna Vashti</span>
    </div>
  </aside>

  <section class="panel front-cover">
    <div class="ornament-border" role="img" aria-label="Light gold swirling filigree border ornament"></div>
    <h1 class="artist-name">Corinna Vashti</h1>
    <div class="cover-photo" role="img" aria-label="Photograph of the artist in shadow beside a tree, light falling on her face"></div>
    <h2 class="album-title">Lift Up Your Lantern</h2>
  </section>
</main>
</body>
</html>
```